TOVR Enterprise
company business card and envolpe design
TOVR Enterprise -
Creative Brief
Professional
Neeraj Pillai
Director
114, 2c, 2nd floor, Rukminibai Market, Rukminibai Bldg No. 6, Pepper Orchard Lane, Mumbai - 400017.
pillaineeraj41@postvela.example
Should look same as the logo. Business card and Stationery should also be very professional.
TOVR Enterprise is the parent company underwhich many other firms are going to start. So back of the card should be designed in way that i can add the name of other firms.

```html
<!DOCTYPE html>
<html lang="en">
<head>
<meta charset="utf-8">
<title>TOVR Enterprise – Business Card</title>
<link rel="stylesheet" href="https://fonts.googleapis.com/css2?family=Open+Sans:wght@400;600;700&display=swap">
<style>
  :root {
    --stage: #2a2a2a;
    --card: #f4f4f4;
    --card-edge: #ffffff;
    --red: #c8161d;
    --red-dark: #9e0f14;
    --grey: #8c8c8c;
    --grey-dark: #5e5e5e;
    --ink: #4a4a4a;
  }
  * { box-sizing: border-box; margin: 0; padding: 0; }
  html, body { width: 1200px; height: 945px; overflow: hidden; }
  body {
    background: var(--stage);
    font-family: "Open Sans", Arial, sans-serif;
    position: relative;
  }
  .card {
    position: absolute;
    width: 520px;
    height: 360px;
    border-radius: 26px;
    background: linear-gradient(180deg, var(--card-edge) 0%, var(--card) 100%);
    overflow: hidden;
  }
  .card--front { left: 140px; top: 140px; }
  .card--back  { left: 541px; top: 505px; }

  .brand {
    display: flex;
    align-items: center;
    gap: 10px;
    color: var(--red);
    font-weight: 700;
    white-space: nowrap;
  }
  .brand__dot {
    border-radius: 50%;
    background: var(--red);
    flex: none;
  }
  .card--front .brand {
    position: absolute;
    top: 50px; left: 0; right: 0;
    justify-content: center;
    font-size: 40px;
    letter-spacing: 1px;
  }
  .card--front .brand__dot { width: 50px; height: 50px; }

  .holder {
    position: absolute;
    top: 130px; left: 0; right: 0;
    text-align: center;
  }
  .holder__name { color: var(--red); font-size: 24px; font-weight: 700; }
  .holder__role { color: var(--ink); font-size: 15px; margin-top: 2px; }

  .band { position: absolute; left: 0; width: 520px; }
  .card--front .band { top: 245px; height: 50px; }
  .card--back .band { top: 300px; height: 40px; }

  .address {
    position: absolute;
    top: 72px; left: 34px;
    font-size: 13px;
    line-height: 19px;
    color: var(--ink);
    font-style: normal;
  }
  .contacts {
    position: absolute;
    top: 182px; left: 34px;
    list-style: none;
    font-size: 13px;
    line-height: 20px;
    color: var(--ink);
  }
  .contacts b { color: var(--red); font-weight: 700; }
  .card--back .brand {
    position: absolute;
    top: 192px; right: 28px;
    font-size: 19px;
    gap: 7px;
  }
  .card--back .brand__dot { width: 26px; height: 26px; }
</style>
</head>
<body>

<section class="card card--front" aria-label="Business card front">
  <div class="brand"><span class="brand__dot"></span>TOVR Enterprise</div>
  <div class="holder">
    <p class="holder__name">Neeraj Pillai</p>
    <p class="holder__role">Director</p>
  </div>
  <svg class="band" viewBox="0 0 520 50" aria-hidden="true">
    <polygon points="0,4 380,4 398,22 0,22" fill="var(--grey)"/>
    <polygon points="0,22 398,22 416,40 0,40" fill="var(--red)"/>
    <polygon points="398,22 520,22 520,25 401,25" fill="var(--red)"/>
  </svg>
</section>

<section class="card card--back" aria-label="Business card back">
  <address class="address">
    114, 2c, 2nd floor, Rukminibai Market,<br>
    Rukminibai Bldg No. 6,<br>
    Pepper Orchard Lane,<br>
    Mumbai - 400017.
  </address>
  <ul class="contacts">
    <li><b>P :</b> +912240158832</li>
    <li><b>C :</b> +919845061297</li>
    <li><b>F :</b> +912240158832</li>
    <li><b>E :</b> pillaineeraj41@postvela.example</li>
  </ul>
  <div class="brand"><span class="brand__dot"></span>TOVR Enterprise</div>
  <svg class="band" viewBox="0 0 520 40" aria-hidden="true">
    <polygon points="0,14 210,14 210,17 0,17" fill="var(--red)"/>
    <polygon points="210,4 520,4 520,17 222,17" fill="var(--grey)"/>
    <polygon points="228,17 520,17 520,32 244,32" fill="var(--red)"/>
  </svg>
</section>

</body>
</html>
```